Need a business card for our overland brand!

We had the logo made and we need a great design for our business card. Use the logo provide or tweak it however you see fit.

Contact Information for Business Card

Name, Title, Telephone, email, website

```html
<!DOCTYPE html>
<html lang="en">
<head>
<meta charset="utf-8">
<title>Sablecrest Treks – Business Card</title>
<link rel="stylesheet" href="https://fonts.googleapis.com/css2?family=Bebas+Neue&family=Oswald:wght@300;400&display=swap">
<style>
  :root {
    --card-bg: #e3e1e4;
    --navy: #1d2a3b;
    --teal-text: #3e97ad;
    --title-grey: #cbc4bd;
    --contact-text: #dde2e7;
    --icon-bg: #1f7fa3;
    --icon-glyph: #0f2533;
  }
  * { margin: 0; padding: 0; box-sizing: border-box; }
  html, body { width: 1200px; height: 734px; overflow: hidden; background: var(--card-bg); }
  .card {
    position: relative;
    width: 1200px;
    height: 734px;
    background: var(--card-bg);
    overflow: hidden;
  }
  .landscape {
    position: absolute;
    left: 0;
    top: 0;
    width: 1200px;
    height: 734px;
  }
  .brand {
    position: absolute;
    right: 150px;
    top: 196px;
    font-family: "Oswald", sans-serif;
    font-weight: 400;
    font-size: 54px;
    line-height: 1;
    letter-spacing: 2px;
    color: var(--navy);
    white-space: nowrap;
  }
  .holder {
    position: absolute;
    left: 117px;
    top: 532px;
  }
  .holder-name {
    font-family: "Bebas Neue", sans-serif;
    font-weight: 400;
    font-size: 74px;
    line-height: 1;
    letter-spacing: 1px;
    color: var(--teal-text);
  }
  .holder-title {
    margin-top: 8px;
    font-family: "Oswald", sans-serif;
    font-weight: 300;
    font-size: 28px;
    letter-spacing: 1.5px;
    color: var(--title-grey);
  }
  .contacts {
    position: absolute;
    left: 694px;
    top: 542px;
    list-style: none;
  }
  .contact {
    display: flex;
    align-items: center;
    height: 30px;
    margin-bottom: 13px;
  }
  .contact-icon { width: 29px; height: 29px; flex: none; }
  .contact-text {
    margin-left: 20px;
    font-family: "Oswald", sans-serif;
    font-weight: 300;
    font-size: 24px;
    letter-spacing: 1.4px;
    color: var(--contact-text);
    white-space: nowrap;
  }
</style>
</head>
<body>
<main class="card">
  <svg class="landscape" role="img" aria-label="Mountain range illustration in teal and navy" viewBox="0 0 1200 734">
    <defs>
      <linearGradient id="range" x1="0" y1="0" x2="0" y2="1">
        <stop offset="0" stop-color="#2a86a6"/>
        <stop offset="0.35" stop-color="#1d2a3b"/>
        <stop offset="1" stop-color="#141d2b"/>
      </linearGradient>
    </defs>
    <rect x="0" y="350" width="1200" height="384" fill="url(#range)"/>
  </svg>

  <h1 class="brand">SABLECREST TREKS</h1>

  <section class="holder">
    <h2 class="holder-name">Daniel Reyes</h2>
    <p class="holder-title">FOUNDER &amp; CEO</p>
  </section>

  <ul class="contacts">
    <li class="contact">
      <svg class="contact-icon" viewBox="0 0 29 29" aria-hidden="true">
        <rect width="29" height="29" rx="5" fill="var(--icon-bg)"/>
        <path d="M9 8c1-1 2-1 3 0l2 3-2 2c1 2 2 3 4 4l2-2 3 2c1 1 1 2 0 3-2 2-5 1-8-2s-5-7-4-10z" fill="var(--icon-glyph)"/>
      </svg>
      <span class="contact-text">(555) 014-2368</span>
    </li>
    <li class="contact">
      <svg class="contact-icon" viewBox="0 0 29 29" aria-hidden="true">
        <rect width="29" height="29" rx="5" fill="var(--icon-bg)"/>
        <rect x="7" y="9" width="15" height="11" rx="1" fill="var(--icon-glyph)"/>
        <path d="M7.5 9.5l7 6 7-6" fill="none" stroke="var(--icon-bg)" stroke-width="1.4"/>
      </svg>
      <span class="contact-text">INFO@SABLECRESTTREKS.COM</span>
    </li>
    <li class="contact">
      <svg class="contact-icon" viewBox="0 0 29 29" aria-hidden="true">
        <rect width="29" height="29" rx="5" fill="var(--icon-bg)"/>
        <circle cx="14.5" cy="14.5" r="7.5" fill="var(--icon-glyph)"/>
        <path d="M7 14.5h15M14.5 7c-3 4-3 11 0 15M14.5 7c3 4 3 11 0 15" fill="none" stroke="var(--icon-bg)" stroke-width="1.2"/>
      </svg>
      <span class="contact-text">SABLECRESTTREKS.COM</span>
    </li>
  </ul>
</main>
</body>
</html>
```